Upmarket Dessert Lounge needs a Business Card Design

We are an upmarket dessert lounge needing a business card to match our image.

We want something that is simple yet beautiful, feminine, classy, sophisticated and elegant. We want it to stand out and don't mind if it is bold.

The design should include our logo and colours of red or maroon with gold highlights. We don't mind if black is used.

Marlow & Quince

Target Market(s)

For those who like to indulge or treat themselves and give in to their temptations on good quality desserts.

Industry/Entity Type

Business

Requirements
Must have
• Must include our logo and our name

Marlow & Quince

M & Q

```html
<!DOCTYPE html>
<html lang="en">
<head>
<meta charset="utf-8">
<title>Marlow &amp; Quince – Business Card</title>
<link href="https://fonts.googleapis.com/css2?family=Libre+Baskerville:wght@400;700&family=Open+Sans:wght@400;600&display=swap" rel="stylesheet">
<style>
  :root {
    --maroon: #7a1517;
    --peach: #fdd4a1;
    --paper: #ffffff;
    --ink: #1e1a18;
    --stage: #ece7e1;
  }
  * { box-sizing: border-box; margin: 0; padding: 0; }
  html, body { width: 1200px; height: 758px; overflow: hidden; }
  body {
    background: var(--stage);
    font-family: "Open Sans", Arial, sans-serif;
    color: var(--ink);
    position: relative;
  }
  .card {
    position: absolute;
    top: 209px;
    width: 540px;
    height: 340px;
    border-radius: 26px;
    overflow: hidden;
    box-shadow: 0 10px 24px rgba(0,0,0,.18);
  }
  .card--front { left: 40px; background: var(--paper); }
  .card--back { left: 620px; background: var(--peach); }

  .brand-name {
    font-family: "Libre Baskerville", Georgia, serif;
    font-weight: 400;
    color: var(--maroon);
    white-space: nowrap;
  }
  .card--front .brand-name {
    position: absolute;
    top: 62px; left: 0; right: 0;
    text-align: center;
    font-size: 30px;
  }

  .info-band {
    position: absolute;
    top: 160px; left: 0; right: 0;
    height: 116px;
    background: var(--peach);
    border-top: 1.5px solid var(--maroon);
    border-bottom: 1.5px solid var(--maroon);
    display: flex;
    align-items: center;
    padding-left: 150px;
  }
  .person { text-align: right; padding-right: 14px; border-right: 1px solid #9a8a7a; }
  .person-name {
    font-family: "Libre Baskerville", Georgia, serif;
    font-weight: 700;
    font-size: 19px;
  }
  .person-title { font-size: 14px; }
  .contact-list { list-style: none; padding-left: 10px; font-size: 14px; line-height: 1.45; }
  .contact-list li { display: flex; align-items: center; gap: 6px; }
  .contact-list svg { width: 12px; height: 12px; fill: var(--ink); flex: none; }

  .address {
    position: absolute;
    bottom: 20px; left: 0; right: 0;
    text-align: center;
    font-size: 15px;
    color: #3a3532;
    letter-spacing: .02em;
  }

  .card--back .monogram {
    position: absolute;
    top: 78px; left: 0; right: 0;
    text-align: center;
    font-size: 84px;
  }
  .card--back .web {
    position: absolute;
    bottom: 56px; left: 0; right: 0;
    text-align: center;
    font-size: 22px;
    letter-spacing: .12em;
  }
</style>
</head>
<body>
  <section class="card card--front">
    <div class="brand-name">Marlow &amp; Quince</div>

    <div class="info-band">
      <div class="person">
        <div class="person-name">Your name</div>
        <div class="person-title">Title</div>
      </div>
      <ul class="contact-list">
        <li><svg viewBox="0 0 12 12"><path d="M3 1l2 2.5-1.2 1.2a6 6 0 003.5 3.5L8.5 7 11 9l-1.3 2C5.5 11 1 6.5 1 2.3z"/></svg>555-014-2780</li>
        <li><svg viewBox="0 0 12 12"><rect x="3" y="0.5" width="6" height="11" rx="1"/><rect x="4" y="2" width="4" height="6" fill="#fdd4a1"/></svg>555-014-2780</li>
        <li><svg viewBox="0 0 12 12"><rect x="0.5" y="2.5" width="11" height="7"/><path d="M0.5 2.5L6 7l5.5-4.5" fill="none" stroke="#fdd4a1" stroke-width="1"/></svg>info@marlowquince.com</li>
        <li><svg viewBox="0 0 12 12"><circle cx="6" cy="6" r="5.5"/><path d="M0.5 6h11M6 .5v11M2 3h8M2 9h8" stroke="#fdd4a1" stroke-width=".8" fill="none"/></svg>www.marlowquince.com</li>
      </ul>
    </div>

    <div class="address">Street Name, City Name, State Zip Code</div>
  </section>

  <section class="card card--back">
    <div class="brand-name monogram">M &amp; Q</div>
    <div class="web">www.marlowquince.com</div>
  </section>
</body>
</html>
```